Ambo postcard design

I am in charge of getting a postcard 5x7 designed for 14 artists having a gallery exhibition. We would like to use our
photo(s) with the 14 names on the front. Back of card would have gallery information.
Am sending jpeg of a past card, four images to choose from and the text for back of card.

```html
<!DOCTYPE html>
<html lang="en">
<head>
<meta charset="utf-8">
<title>The Ambo Group – Exhibition Postcard</title>
<link rel="stylesheet" href="https://fonts.googleapis.com/css2?family=Satisfy&family=Poppins:wght@400;600&display=swap">
<style>
  :root {
    --paper: #ffffff;
    --wood-dark: #4a1f0e;
    --wood-mid: #7a3a1c;
    --wood-light: #9a5430;
    --text-light: #ffffff;
    --shadow: rgba(30, 10, 0, 0.75);
    --info-box: #c9c7c3;
    --info-border: #a9a6a1;
    --info-text: #3a1d10;
  }
  * { margin: 0; padding: 0; box-sizing: border-box; }
  html, body {
    width: 1200px;
    height: 863px;
    overflow: hidden;
    background: var(--paper);
  }
  .postcard {
    position: relative;
    width: 1200px;
    height: 863px;
    background: var(--paper);
  }
  .wood-panel {
    position: absolute;
    left: 21px;
    top: 21px;
    width: 1157px;
    height: 820px;
    background:
      linear-gradient(180deg, rgba(0,0,0,0.15) 0%, rgba(0,0,0,0) 30%, rgba(0,0,0,0.1) 100%),
      linear-gradient(90deg, var(--wood-dark) 0%, var(--wood-mid) 25%, var(--wood-light) 50%, var(--wood-mid) 75%, var(--wood-dark) 100%);
  }
  .text-column {
    position: absolute;
    left: 21px;
    width: 583px;
    text-align: center;
    color: var(--text-light);
    text-shadow: 1px 2px 3px var(--shadow);
  }
  .gallery-title {
    top: 96px;
    font-family: "Satisfy", cursive;
    font-size: 60px;
    font-weight: 400;
    line-height: 1;
  }
  .presents {
    top: 188px;
    font-family: "Poppins", sans-serif;
    font-size: 19px;
    font-weight: 400;
  }
  .exhibition-details, .gallery-contact {
    font-family: "Poppins", sans-serif;
    font-size: 21px;
    font-weight: 600;
    letter-spacing: 0.6px;
  }
  .exhibition-details { top: 286px; line-height: 29px; }
  .gallery-contact { top: 427px; line-height: 28.5px; }
  .info-box {
    position: absolute;
    left: 21px;
    top: 657px;
    width: 583px;
    height: 159px;
    background: var(--info-box);
    border: 2px solid var(--info-border);
    box-shadow: 0 2px 4px rgba(0,0,0,0.4);
    color: var(--info-text);
    font-family: "Poppins", sans-serif;
    font-size: 18.5px;
    font-weight: 600;
    line-height: 25.8px;
    text-align: center;
    padding-top: 15px;
  }
</style>
</head>
<body>
  <main class="postcard">
    <div class="wood-panel" role="img" aria-label="Warm brown vertical wood-grain background"></div>

    <h1 class="text-column gallery-title">Gallery Cellar</h1>
    <p class="text-column presents">presents an exhibition by</p>

    <div class="text-column exhibition-details">
      <p>“The Ambo Group”</p>
      <p>September 28th - October 31, 2015</p>
      <p>Reception - Friday, October 2, 5-8pm</p>
    </div>

    <address class="text-column gallery-contact" style="font-style: normal;">
      <p>Gallery Cellar</p>
      <p>Quartz Row Shops, 1400 Quartz Drive</p>
      <p>Fairbrook, Virginia 22000</p>
      <p>555-010-0652</p>
      <p>info@gallerycellar.org</p>
      <p>www.gallerycellar.org</p>
    </address>

    <div class="info-box">
      <p>Gallery Hours: M-F 10:00am-6:00pm</p>
      <p>Saturday 10:00am-2pm. Parking is available</p>
      <p>in metered spots on nearby streets</p>
      <p>and in public garages</p>
      <p>(free on weekends and after 4pm weekdays)</p>
    </div>
  </main>
</body>
</html>
```